Exciting Poster Project: 4 posters for Employee Benefit Program

We are an entrepreneurial healthcare IT company that is creating an internal campaign to launch our 2017 Culture and Professional Development goals for our internal staff.

We need 4 posters utilizing the 4 campaign logos (attached) that are tied together visually into a cohesive campaign.

A PPT is included that shows the other wall art that currently exists on the walls. The new posters will share a space with these pieces.

The posters may be mounted side by side, or stand alone on a wall- so the design should work both ways. Each poster should include its own icon and the tag line provided along with topics provided that fall under this category. The posters size can be dictated by your design, but the text should be legible from a minimum of 8 feet away.

At the bottom of each poster should include all 4 icons in order to tie the entire campaign together (perhaps they can be arranged together like a diamond shape with the primary one as the biggest diamond)

Our company website for our external branding is: www.pelmaroq.com
We have included our branding guidelines for our external brand, and ppts and graphics for our internal brand.

1) Poster 1:
a. Header: Better Today Than Yesterday
b. Sub-title: Personal and Professional Growth
c. Description: We are committed to helping you build on your strengths and passions and support you your career advancement goals. We have a variety of training and development programs available to help you reach your top potential!
Leadership Development Programs
1. Supervisor Training
2. Women’s Leadership
3. Leadership Meet-Ups
4. MBA Program
Staff Development
1. Continuing Education Fund
2. Book Club
3. Pelmaroq University
4. Mentorship
5. Learning Libraries
6. Department Wide Training Events

2) Poster 2:
a. Header: Perform at Highest Capacity
b. Sub-title: Be Your Best Self
c. Description: We are committed to providing programs that bring focus to your health and overall personal wellness to encourage a well balanced life
i. Healthy Living
1. Health and wellness seminars
2. Nutrition: Fruit Delivery
ii. Fitness:
1. Step Challenge
2. Virtual 5k
3. Recess
4. Golf Lessons
5. Ping Pong Club
iii. Creativity:
1. Painting
2. Photography Club
3. Virtual Trivia
iv. Mental Health:
1. Massage Therapy
2. EAP Education
v. Financial
1. 401(k)
2. Retirement education/financial planning seminars
3. Global Insurance Program education

3) Poster 3:
a. Header: Passionate Urgent and Driven to Success
b. Sub-Header: Innovation and Strategy
c. Description: We are committed to helping you connect the dots both in the industry and with our internal goals , mission, and vision.
i. Quarterly All-Hands
ii. Lumiverse
1. Internally: Departmental and Product Updates
2. Externally: Industry Knowledge
3. Culturally: Peer to Peer Community

4) Poster 4:
a. Header: Succeed as a Team
b. Sub-Header: Cultivating Collaboration
c. Description: We are committed to creating a culture of appreciation, teamwork, and supporting an open communication. All feedback and ideas are welcome here!
i. Team Building Events
1. Employee Focused
a. Summer Picnic
b. Employee Appreciation
c. Diwali
d. Holiday Party
e. Department Appreciation
2. Family Friendly
a. Halloween
b. Bring your Kids to Work Day
3. Awards
a. Peer to Peer: QuickNod Awards
b. Leadership: Crest of Merit
4. Surveys
a. New Hire
b. Employee Engagement
Updates

Target Market(s)

Internal Employees

Industry/Entity Type

Healthcare

Font styles to use
Sans Serif

Requirements
Must have
• Job Type: Posters
• Task Outline: Create Vector Art for 4 icons and 4 posters
• Fonts and Styles to Use: SourceSansPro
Nice to have
• There is an attachment with suggested concepts and styles that we like.
Should not have
• The poster should not be very wordy or hard to read in passing.

```html
<!DOCTYPE html>
<html lang="en">
<head>
<meta charset="utf-8">
<title>Better Today Than Yesterday — Personal and Professional Growth</title>
<link rel="stylesheet" href="https://fonts.googleapis.com/css2?family=Graduate&family=Cabin:wght@400;600&display=swap">
<style>
  :root {
    --blue-top: #2459ae;
    --blue-bottom: #1d4c9c;
    --blue-ink: #2a5cb0;
    --sky: #6ab2dc;
    --paper: #f1f1f1;
    --ink: #161616;
    --white: #ffffff;
  }
  html, body {
    margin: 0;
    width: 1000px;
    height: 1200px;
    overflow: hidden;
    background: var(--paper);
  }
  .poster {
    position: relative;
    width: 1000px;
    height: 1200px;
    overflow: hidden;
    background: linear-gradient(180deg, var(--blue-top), var(--blue-bottom));
    font-family: "Cabin", sans-serif;
  }
  .poster-shapes {
    position: absolute;
    inset: 0;
  }
  .headline {
    position: absolute;
    top: 38px;
    left: 0;
    width: 1000px;
    margin: 0;
    text-align: center;
    font-family: "Graduate", serif;
    font-weight: 400;
    font-size: 66px;
    line-height: 86px;
    color: var(--white);
    letter-spacing: 1px;
  }
  .subtitle {
    position: absolute;
    top: 206px;
    right: 148px;
    margin: 0;
    text-align: right;
    font-weight: 400;
    font-size: 47px;
    line-height: 48px;
    color: var(--white);
  }
  .intro {
    position: absolute;
    top: 330px;
    left: 356px;
    width: 504px;
    margin: 0;
    font-size: 24px;
    line-height: 27.5px;
    text-align: justify;
    color: var(--white);
  }
  .program {
    position: absolute;
    width: 400px;
    text-align: center;
    color: var(--ink);
  }
  .program-title {
    margin: 0 0 4px;
    font-weight: 600;
    font-size: 25px;
    line-height: 33px;
    color: var(--blue-ink);
  }
  .program-list {
    list-style: none;
    margin: 0;
    padding: 0;
    font-size: 25.5px;
    line-height: 33.5px;
  }
  .program--staff { left: 317px; top: 530px; }
  .program--leadership { left: 46px; top: 810px; }
</style>
</head>
<body>
<main class="poster">
  <svg class="poster-shapes" width="1000" height="1200" viewBox="0 0 1000 1200" aria-hidden="false">
    <defs>
      <linearGradient id="puzzle-tone" x1="0" y1="0" x2="1" y2="1">
        <stop offset="0" stop-color="#eef1f5"/>
        <stop offset="1" stop-color="#6ab2dc"/>
      </linearGradient>
    </defs>
    <rect class="figure-area" x="0" y="182" width="320" height="690" fill="#ffffff" fill-opacity="0.16"
          role="img" aria-label="White pictogram of a person raising one arm in achievement"/>
    <rect class="puzzle-area" x="605" y="590" width="395" height="610" fill="url(#puzzle-tone)"
          role="img" aria-label="Interlocking white and light blue puzzle pieces"/>
    <circle class="badge badge--staff" cx="517" cy="694" r="200" fill="#f2f2f2"/>
    <circle class="badge badge--leadership" cx="246" cy="966" r="200" fill="#f2f2f2"/>
    <path class="connector" d="M464 872 C 462 940, 520 905, 540 950 S 580 985, 610 979" fill="none" stroke="#ffffff" stroke-width="5"/>
    <path class="connector-inner" d="M464 872 C 462 940, 520 905, 540 950 S 580 985, 610 979" fill="none" stroke="#2a5cb0" stroke-width="2"/>
    <rect class="cap-area" x="420" y="815" width="92" height="60" fill="#2a5cb0"
          role="img" aria-label="Graduation cap icon"/>
    <rect class="books-area" x="105" y="1058" width="72" height="76" fill="#2a5cb0"
          role="img" aria-label="Icon of books standing on a shelf"/>
  </svg>

  <h1 class="headline">BETTER TODAY<br>THAN&nbsp; YESTERDAY</h1>
  <h2 class="subtitle">Personal and<br>Professional Growth</h2>
  <p class="intro">We are committed to helping you build on your strengths and passions and support you your career advancement goals. We have a variety of training and development programs available to help you reach your top potential!</p>

  <section class="program program--staff">
    <h3 class="program-title">STAFF<br>DEVELOPMENT</h3>
    <ul class="program-list">
      <li>Continuing Education Fund</li>
      <li>Book Club</li>
      <li>Pelmaroq University</li>
      <li>Mentorship</li>
      <li>Learning Libraries</li>
      <li>Wide Training Events</li>
    </ul>
  </section>

  <section class="program program--leadership">
    <h3 class="program-title">LEADERSHIP<br>DEVELOPMENT<br>PROGRAMS</h3>
    <ul class="program-list">
      <li>Supervisor Training</li>
      <li>Women’s Leadership</li>
      <li>Leadership Meet-Ups</li>
      <li>MBA Program</li>
    </ul>
  </section>
</main>
</body>
</html>
```